Larkfield Clinic Booklet 2016

Larkfield Clinic is a multi-specialty Practice in Midtown Manhattan offering advanced care in multiple areas of medicine. See our table of contents (PDF Uploaded)
Our designed booklet should be clean, easy to read, contemporary, high-end and elegant.
We need a general theme, Layout for cover and templates for internal.
We are entertaining the idea of two different sizes
8 x 10
or
11 x 8.5
Our tagline " The Future of Medicine is Here"
We will provide all the text content
The link to our website
www.LarkfieldCL.example
Uploaded files are as follows.. Logo, Our Team Photo and the PDF listing the table of contents.

```html
<!DOCTYPE html>
<html lang="en">
<head>
<meta charset="utf-8">
<title>Larkfield Clinic Booklet Cover</title>
<link href="https://fonts.googleapis.com/css2?family=Josefin+Sans:wght@400&family=Roboto+Slab:wght@300&family=Montserrat:wght@500&display=swap" rel="stylesheet">
<style>
  :root {
    --backdrop: #c9cacc;
    --paper: #ffffff;
    --paper-shade: #f3f4f6;
    --sky: #a8bfe2;
    --navy: #2d3350;
    --ink: #2b2f45;
    --hex-line: #d9dbe1;
  }
  html, body {
    margin: 0;
    padding: 0;
    width: 1200px;
    height: 857px;
    overflow: hidden;
    background: var(--backdrop);
  }
  .spread {
    position: absolute;
    left: 180px;
    top: 131px;
    width: 840px;
    height: 594px;
    display: flex;
    box-shadow: 0 6px 24px rgba(0,0,0,0.18);
  }
  .page {
    position: relative;
    width: 420px;
    height: 594px;
    background: var(--paper);
    overflow: hidden;
  }
  .page--back { background: linear-gradient(90deg, var(--paper) 85%, var(--paper-shade)); }
  .page--front { background: linear-gradient(90deg, var(--paper-shade), var(--paper) 12%); }

  .back-band {
    position: absolute;
    left: 0;
    top: 118px;
    width: 100%;
    height: 104px;
    background: var(--sky);
  }
  .brand {
    position: absolute;
    display: flex;
    flex-direction: column;
    align-items: center;
    gap: 8px;
  }
  .brand__mark {
    width: 40px;
    height: 40px;
    border-radius: 50%;
    background: var(--navy);
  }
  .brand__name {
    font-family: "Josefin Sans", sans-serif;
    font-weight: 400;
    font-size: 17px;
    line-height: 1.05;
    letter-spacing: 0.5px;
    color: var(--ink);
    text-align: center;
    text-transform: uppercase;
  }
  .page--back .brand { left: 130px; top: 350px; width: 160px; }
  .page--front .brand { left: 250px; top: 318px; width: 150px; }

  .web-address {
    position: absolute;
    font-family: "Montserrat", sans-serif;
    font-weight: 500;
    font-size: 8px;
    letter-spacing: 3.2px;
    color: var(--ink);
    text-transform: lowercase;
  }
  .page--back .web-address { left: 82px; top: 520px; }
  .page--front .web-address { left: 52px; top: 492px; }

  .cover-art {
    position: absolute;
    left: 0;
    top: 0;
  }
  .tagline {
    position: absolute;
    right: 34px;
    top: 30px;
    font-family: "Roboto Slab", serif;
    font-weight: 300;
    font-size: 17px;
    line-height: 1.2;
    color: var(--paper);
  }
</style>
</head>
<body>
  <main class="spread">
    <section class="page page--back" aria-label="Back cover">
      <div class="back-band"></div>
      <div class="brand">
        <div class="brand__mark"></div>
        <div class="brand__name">Larkfield<br>Clinic</div>
      </div>
      <p class="web-address" style="margin:0">www.larkfieldcl.example</p>
    </section>

    <section class="page page--front" aria-label="Front cover">
      <svg class="cover-art" width="420" height="594" viewBox="0 0 420 594">
        <polygon class="corner-wedge" points="150,0 420,0 420,250" fill="var(--sky)"/>
        <polygon class="hex-outline" points="150,74 258,136 258,262 150,324 42,262 42,136"
                 fill="none" stroke="var(--hex-line)" stroke-width="1.5"/>
        <polygon class="hex-frame" points="150,30 272,100 272,240 150,310 28,240 28,100"
                 fill="var(--navy)"/>
        <polygon class="team-photo" role="img" aria-label="Team photo of clinic staff in blue scrubs"
                 points="150,46 258,108 258,232 150,294 42,232 42,108"
                 fill="url(#photoTone)"/>
        <defs>
          <linearGradient id="photoTone" x1="0" y1="0" x2="0" y2="1">
            <stop offset="0" stop-color="#b9bcc4"/>
            <stop offset="0.45" stop-color="#8ea6cc"/>
            <stop offset="1" stop-color="#6f8fc2"/>
          </linearGradient>
        </defs>
      </svg>
      <p class="tagline" style="margin:0">The Future of<br>Medicine is Here</p>
      <div class="brand">
        <div class="brand__mark"></div>
        <div class="brand__name">Larkfield<br>Clinic</div>
      </div>
      <p class="web-address" style="margin:0">www.larkfieldcl.example</p>
    </section>
  </main>
</body>
</html>
```